Fern Otter Sunscreen & Insect Repellent Design for Spray Can

A new product launch.

New Product: Fern Otter SPF 30 & Natural Insect Repellent

Background Colors to use: Green & Yellow

- Existing Die line for our SPF 50 & Image of Product - to show how the product translates from Dieline to Can.
- New Die Line with Logo / Call Outs / *Add Color/Font/Design

Leave the Fern Otter Logo at top of can.

Target Market(s)

Outdoor Market. We make unique essentials for Outdoor Sport, Travel & Adventure.

Industry/Entity Type

Product

```html
<!DOCTYPE html>
<html lang="en">
<head>
<meta charset="utf-8">
<title>Fern Otter SPF 30 &amp; Natural Insect Repellent – Spray Can</title>
<link href="https://fonts.googleapis.com/css2?family=Russo+One&family=Oswald:wght@500;600&family=Lato:wght@400;700&display=swap" rel="stylesheet">
<style>
  :root{
    --bg:#ffffff;
    --can-deep:#0f2e12;
    --can-mid:#1f5a22;
    --can-light:#3c8a35;
    --cap:#eceeed;
    --cap-shade:#d8dcdb;
    --brand-white:#ffffff;
    --callout-yellow:#f3e51a;
    --accent-orange:#e8823a;
    --label-white:#ffffff;
    --label-ink:#5a5a5a;
    --rule:#bdbdbd;
  }
  *{margin:0;padding:0;box-sizing:border-box}
  html,body{width:1200px;height:1200px;overflow:hidden;background:var(--bg)}
  .canvas{position:relative;width:1200px;height:1200px}
  .cans{position:absolute;inset:0}
  .front, .back{position:absolute;left:0;top:0;width:1200px;height:1200px}
  .center{position:absolute;text-align:center;transform:translateX(-50%);white-space:nowrap}

  /* front panel */
  .brand-mark{position:absolute;left:378px;top:505px;width:150px;height:150px;border-radius:50%;
    background:var(--accent-orange);transform:translateX(-50%);opacity:.9}
  .brand-name{font-family:"Russo One",sans-serif;color:var(--brand-white);font-size:48px;line-height:46px;letter-spacing:1px}
  .spf{font-family:"Oswald",sans-serif;font-weight:600;color:var(--callout-yellow);font-size:23px;line-height:26px}
  .headline{font-family:"Oswald",sans-serif;font-weight:600;color:var(--brand-white);font-size:29px;line-height:34px;letter-spacing:0}
  .headline.yellow{color:var(--callout-yellow);font-size:31px}
  .with{font-family:"Lato",sans-serif;color:var(--brand-white);font-size:17px}
  .benefit{font-family:"Lato",sans-serif;color:var(--accent-orange);font-size:17px;line-height:19px}
  .protection{font-family:"Oswald",sans-serif;font-weight:600;color:var(--callout-yellow);font-size:22px;line-height:32px}
  .net{font-family:"Lato",sans-serif;font-weight:700;color:var(--brand-white);font-size:15px}

  /* back panel */
  .back-mark{position:absolute;left:802px;top:505px;width:62px;height:62px;border-radius:50%;
    background:var(--accent-orange);transform:translateX(-50%);opacity:.9}
  .back-name{font-family:"Russo One",sans-serif;color:var(--brand-white);font-size:19px;line-height:18px}
  .drug-label{position:absolute;left:690px;top:606px;width:224px;height:486px;background:var(--label-white);
    border-radius:2px;overflow:hidden;
    padding:9px 8px 6px;font-family:"Lato",sans-serif;color:var(--label-ink);font-size:6.8px;line-height:9px}
  .drug-label p{margin-bottom:3px}
  .label-band{background:var(--accent-orange);color:#fff;font-weight:700;font-size:7px;line-height:10px;padding:1px 4px;margin:4px 0 3px}
  .label-band.title{text-align:center;font-size:7.5px;padding:2px 4px;margin:5px 0 5px}
  .active-row{display:flex;justify-content:space-between;border-bottom:.5px dotted var(--rule)}
  .drug-label ul{list-style:disc;padding-left:9px;margin-bottom:3px}
</style>
</head>
<body>
<main class="canvas">
  <svg class="cans" width="1200" height="1200" viewBox="0 0 1200 1200" aria-hidden="true">
    <defs>
      <radialGradient id="canGlow" cx="0.5" cy="0.3" r="0.8">
        <stop offset="0" stop-color="var(--can-light)"/>
        <stop offset="0.55" stop-color="var(--can-mid)"/>
        <stop offset="1" stop-color="var(--can-deep)"/>
      </radialGradient>
    </defs>
    <rect x="305" y="115" width="150" height="165" rx="28" fill="var(--cap)"/>
    <rect x="318" y="262" width="124" height="26" rx="4" fill="var(--cap-shade)"/>
    <path d="M262 345 Q262 285 330 285 L428 285 Q495 285 495 345 L495 1085 Q495 1105 475 1105 L282 1105 Q262 1105 262 1085 Z" fill="url(#canGlow)"/>
    <rect x="720" y="115" width="142" height="160" rx="26" fill="var(--cap)"/>
    <rect x="732" y="258" width="118" height="24" rx="4" fill="var(--cap-shade)"/>
    <path d="M684 340 Q684 282 748 282 L856 282 Q920 282 920 340 L920 1080 Q920 1100 900 1100 L704 1100 Q684 1100 684 1080 Z" fill="url(#canGlow)"/>
  </svg>

  <section class="front">
    <div class="brand-mark"></div>
    <div class="center brand-name" style="left:378px;top:674px">FERN<br>OTTER</div>
    <div class="center spf" style="left:378px;top:780px">SPF 30</div>
    <div class="center headline" style="left:378px;top:806px">NATURAL INSECT</div>
    <div class="center headline yellow" style="left:378px;top:840px">REPELLENT</div>
    <div class="center with" style="left:378px;top:890px">with</div>
    <div class="center benefit" style="left:378px;top:912px">cooling aloe<br>Broad Spectrum</div>
    <div class="center protection" style="left:378px;top:982px">UVA &amp; UVB Protection<br>Vitamins A &amp; E</div>
    <div class="center net" style="left:378px;top:1068px">6 oz./ 177 ml.</div>
  </section>

  <section class="back">
    <div class="back-mark"></div>
    <div class="center back-name" style="left:802px;top:566px">FERN<br>OTTER</div>
    <div class="drug-label">
      <p>Continuous spray gives even sun protection for active skin outdoors. Suitable for ages six months and up.</p>
      <div class="label-band title">SPF 50 SUNSCREEN CONTINUOUS SPRAY</div>
      <p>Drug Facts</p>
      <div class="label-band active-row"><span>Active ingredients</span><span>Purpose</span></div>
      <div class="active-row"><span>Avobenzone 3.0%</span><span>Sunscreen</span></div>
      <div class="active-row"><span>Homosalate 10.0%</span><span>Sunscreen</span></div>
      <div class="active-row"><span>Octisalate 5.0%</span><span>Sunscreen</span></div>
      <div class="active-row"><span>Octocrylene 10.0%</span><span>Sunscreen</span></div>
      <div class="active-row" style="margin-bottom:3px"><span>Oxybenzone 6.0%</span><span>Sunscreen</span></div>
      <div class="label-band">Uses</div>
      <p>Helps prevent sunburn. Used with other sun measures, lowers skin risk.</p>
      <div class="label-band">Warnings</div>
      <p>For external use only.</p>
      <p>Flammable. Keep away from heat and flame.</p>
      <p>When using: keep out of eyes. Rinse with water.</p>
      <p>Stop use if rash appears.</p>
      <p>Keep out of reach of children.</p>
      <div class="label-band">Directions</div>
      <ul>
        <li>Apply generously 15 minutes before sun.</li>
        <li>Reapply after 80 minutes of swimming.</li>
        <li>Reapply at least every two hours.</li>
        <li>Limit time in sun 10 a.m. – 2 p.m.</li>
        <li>Wear long sleeves, hats and sunglasses.</li>
        <li>Children under 6 months: ask a doctor.</li>
      </ul>
      <div class="label-band">Other information</div>
      <p>Protect from excessive heat.</p>
      <div class="label-band">Inactive ingredients</div>
      <p>Alcohol, aloe leaf juice, tocopherol, retinyl palmitate, fragrance.</p>
      <div class="label-band">Questions or comments</div>
      <p>Fern Otter Co. 120 Cedar Lane Boulder CO 80302<br>800 555 0142 www.fernotterco.com</p>
    </div>
  </section>
</main>
</body>
</html>
```